Verdo Studios Business Card

Business card for video production company, I want to give the impression of quality, It has to stand out for its design; it has to be easily readable and please avoid any extravaganza!. I'm looking for a first impression, then the card goes to the trash.

You guys have complete freedom of design! background color, logo colors etc
you can choose one side card or two sided, die cut also a possibility .
Just let me know for what kind of card is your design.
In the files you will find the logo .ai to modify it.

One of the differences between the ambiguous terms Filmmaker and videographer is that filmmaking is more arty, we tend to leave backgrounds out of focus, we create different layers or points of attention with our lens.

Logo
Stories Shot With Care
www.verdostudios-example.com
www.socialpage-example.com/verdostudios
tomas@verdostudios-example.com
555-318-6092
Add QR Code

```html
<!DOCTYPE html>
<html lang="en">
<head>
<meta charset="utf-8">
<title>Verdo Studios Business Card</title>
<link href="https://fonts.googleapis.com/css2?family=Open+Sans:wght@400;700&display=swap" rel="stylesheet">
<style>
  :root {
    --page-bg: #c9c6c6;
    --card-bg: #2a2627;
    --mark-grey: #9a9a9c;
    --brand-red: #e3262c;
    --text-white: #ffffff;
  }
  * { margin: 0; padding: 0; box-sizing: border-box; }
  html, body {
    width: 1200px;
    height: 900px;
    overflow: hidden;
    background: var(--page-bg);
    font-family: "Open Sans", Arial, sans-serif;
  }
  .canvas {
    position: relative;
    width: 1200px;
    height: 900px;
  }
  .card {
    position: absolute;
    width: 620px;
    height: 354px;
    background: var(--card-bg);
    overflow: hidden;
  }
  .card--front { left: 70px; top: 80px; }
  .card--back { left: 510px; top: 466px; }

  .brand {
    position: absolute;
    left: 0;
    right: 0;
    display: flex;
    flex-direction: column;
    align-items: center;
  }
  .brand__square {
    width: 62px;
    height: 46px;
    border-radius: 10px;
  }
  .brand__name {
    margin-top: 10px;
    font-weight: 700;
    font-size: 38px;
    line-height: 46px;
    letter-spacing: 4px;
    text-transform: uppercase;
    white-space: nowrap;
  }
  .card--front .brand { top: 112px; }
  .card--front .brand__square { background: var(--mark-grey); }
  .card--front .brand__name { color: var(--mark-grey); }

  .card--back .brand { top: 40px; }
  .card--back .brand__square { background: var(--text-white); }
  .card--back .brand__name { color: var(--brand-red); }

  .contact {
    position: absolute;
    left: 150px;
    top: 168px;
    color: var(--text-white);
    font-size: 19px;
    line-height: 25px;
    white-space: nowrap;
  }
  .contact__tagline { padding-left: 50px; }
  .contact__row { display: flex; }
  .contact__label { width: 50px; flex: none; }
</style>
</head>
<body>
<main class="canvas">
  <section class="card card--front" aria-label="Card front">
    <div class="brand">
      <div class="brand__square"></div>
      <div class="brand__name">Verdo Studios</div>
    </div>
  </section>

  <section class="card card--back" aria-label="Card back">
    <div class="brand">
      <div class="brand__square"></div>
      <div class="brand__name">Verdo Studios</div>
    </div>
    <div class="contact">
      <p class="contact__tagline">Stories Shot With Care</p>
      <p class="contact__row"><span class="contact__label">W :</span><span>www.verdostudios-example.com</span></p>
      <p class="contact__row"><span class="contact__label"></span><span>www.socialpage-example.com/verdostudios</span></p>
      <p class="contact__row"><span class="contact__label">E :</span><span>tomas@verdostudios-example.com</span></p>
      <p class="contact__row"><span class="contact__label">S :</span><span>555-318-6092</span></p>
    </div>
  </section>
</main>
</body>
</html>
```